Memorial page to show case the life and works of an individual who has passed

I would like to design a website as a memorial page for my mother. She was a very senior member of the London community and would like to design something that has a page for her biography. Gallery. Testimonials. Etc. Something that is smart and modern.
similar to
http://www.gervaldquinnstudio.org/
Not to have things that are flowery it need to be a website that is smart clean and proffesional to showcase the life and works of an indiviudal

there wont be a logo as it is not a company

Industry/Entity Type

Community

Number of Pages Required

4 page

Colors
9bcb3c
abd036
ffffff
f78f20
3176b5

Requirements
Must have
• Gallary
• moving gallary at the top
• About
• Testimonials
• Videos
• Leave a message

```html
<!DOCTYPE html>
<html lang="en">
<head>
<meta charset="utf-8">
<title>Edith Harrow — In Memory</title>
<link rel="stylesheet" href="https://fonts.googleapis.com/css2?family=Encode+Sans+Condensed:wght@300;400&family=Open+Sans:wght@400;600&family=Playfair+Display:ital@1&display=swap">
<style>
  :root {
    --backdrop: #857d7c;
    --page: #ffffff;
    --accent-green: #abd036;
    --accent-lime: #9bcb3c;
    --nav-line: #8a8a8a;
    --text-dark: #4a4a4a;
    --text-body: #777777;
    --text-muted: #8d8d8d;
    --divider: #b9b39a;
    --hero-dark: #3c3433;
    --hero-warm: #5a4644;
  }
  * { box-sizing: border-box; margin: 0; padding: 0; }
  html, body { width: 1200px; height: 900px; overflow: hidden; }
  body { background: var(--backdrop); font-family: "Open Sans", Arial, sans-serif; position: relative; }

  .page { position: absolute; left: 160px; top: 44px; width: 840px; height: 806px; background: var(--page); }

  .main-nav { position: absolute; top: 44px; left: 246px; display: flex; gap: 10px; }
  .main-nav a {
    display: block; width: 64px; padding-top: 4px; border-top: 2px solid var(--nav-line);
    font-size: 9.5px; color: var(--text-dark); text-decoration: none; text-align: center; letter-spacing: .2px;
  }
  .main-nav a.is-current { border-top-color: var(--accent-green); color: var(--accent-lime); }
  .main-nav a.wide { width: 70px; }

  .hero {
    position: absolute; left: 58px; top: 68px; width: 746px; height: 224px;
    background: linear-gradient(90deg, var(--hero-dark) 0%, var(--hero-warm) 60%, #6d4f4d 100%);
  }
  .hero-portrait {
    position: absolute; left: 144px; top: 34px; width: 250px; height: 162px;
    background: linear-gradient(120deg, #d9b12a 0%, #c9a64a 35%, #b9b7ad 60%, #8c9a86 100%);
  }
  .hero-name {
    position: absolute; left: 410px; top: 78px; color: #fff; font-weight: 400;
    font-family: "Playfair Display", Georgia, serif; font-style: italic; font-size: 21px; line-height: 32px; letter-spacing: .5px;
  }

  .tagline {
    position: absolute; top: 326px; left: 0; width: 840px; text-align: center;
    font-family: "Encode Sans Condensed", "Arial Narrow", sans-serif; font-weight: 300; font-size: 19px; color: var(--text-dark);
  }

  .intro-crest { position: absolute; left: 204px; top: 366px; width: 50px; height: 50px; background: #d8c46b; border-radius: 40% 40% 50% 50%; }
  .intro-summary {
    position: absolute; left: 152px; top: 434px; width: 154px; text-align: center;
    font-size: 8.5px; line-height: 12px; color: var(--text-body);
  }
  .intro-summary p + p { margin-top: 12px; }
  .intro-divider { position: absolute; left: 316px; top: 366px; width: 1px; height: 190px; background: var(--divider); }
  .biography {
    position: absolute; left: 330px; top: 370px; width: 450px;
    font-size: 8.5px; line-height: 12px; color: var(--text-body); text-align: justify;
  }
  .biography p + p { margin-top: 12px; }

  .gallery { position: absolute; left: 188px; top: 576px; width: 508px; height: 90px; }
  .gallery-photo { position: absolute; top: 0; height: 90px; border: 3px solid #222; }
  .gallery-arrow { position: absolute; top: 35px; }

  .site-footer { position: absolute; left: 180px; top: 684px; display: flex; align-items: center; gap: 8px; font-size: 8.5px; color: var(--text-muted); }
  .footer-mark { width: 20px; height: 20px; border-radius: 50%; background: #e2d34c; }
</style>
</head>
<body>
  <div class="page">
    <nav class="main-nav">
      <a href="#" class="is-current">HOME</a>
      <a href="#">ABOUT HER</a>
      <a href="#">STORIES</a>
      <a href="#" class="wide">TESTIMONIALS</a>
      <a href="#">CONTACT</a>
    </nav>

    <header class="hero" role="img" aria-label="Soft autumn park background">
      <div class="hero-portrait" role="img" aria-label="Portrait of Edith Harrow smiling in an autumn park"></div>
      <h1 class="hero-name">EDITH HARROW<br>1935 - 2016</h1>
    </header>

    <p class="tagline">friend . . .mother. . . grandmother . . . great-grandmother . . . baker</p>

    <div class="intro-crest" role="img" aria-label="Decorative crest ornament"></div>
    <div class="intro-summary">
      <p>EDITH HARROW, born July 18, 1935</p>
      <p>A beautiful and happy woman who made everyone she met feel like the only person existed. Edith cared about everyone.</p>
      <p>She sadly left us January 3, 2016. She will always be remembered by her all friends and family.</p>
    </div>
    <div class="intro-divider"></div>
    <section class="biography">
      <p>Edith Harrow grew up in a small terraced house in east London, the eldest of four children. She learned to bake at her grandmother's side and never stopped. For fifty years her kitchen was open to neighbours, friends and strangers alike, and her table was always full. She served on the parish council, ran the Saturday market stall and raised funds for the local library. Those who knew her remember a quick laugh, a firm hand and a tin of fresh scones kept ready for anyone who knocked.</p>
      <p>In later years she became a mentor to young families arriving in the borough, helping them find schools, work and a place to belong. She was honoured by the community trust in 2009 for a lifetime of service. Her children, grandchildren and great-grandchildren carry on her recipes and her habit of welcoming everyone. This page gathers her stories, photographs and the memories shared by the many people whose lives she touched. Please take a moment to read, to remember and to leave a message of your own.</p>
    </section>

    <div class="gallery">
      <div class="gallery-photo" style="left:0;width:40px;background:linear-gradient(135deg,#7d8fa3,#c9c2bd);" role="img" aria-label="Gallery photo of Edith outdoors"></div>
      <div class="gallery-photo" style="left:52px;width:120px;background:linear-gradient(135deg,#8a6a5c,#d8cfc6 60%,#6b5a50);" role="img" aria-label="Gallery photo of Edith with a friend"></div>
      <div class="gallery-photo" style="left:180px;width:120px;background:linear-gradient(135deg,#c8c3bd,#e6e0d9 50%,#9b8a7e);" role="img" aria-label="Gallery photo of Edith with her husband"></div>
      <div class="gallery-photo" style="left:308px;width:120px;background:linear-gradient(135deg,#1f7f96,#5fb4c6 50%,#2c6d7d);" role="img" aria-label="Gallery photo of Edith swimming"></div>
      <div class="gallery-photo" style="left:438px;width:66px;background:linear-gradient(135deg,#6d8aa3,#d0cbc6);" role="img" aria-label="Gallery photo of Edith at home"></div>
      <svg class="gallery-arrow" style="left:-4px" width="12" height="20" viewBox="0 0 12 20"><polyline points="10,2 2,10 10,18" fill="none" stroke="#fff" stroke-width="2"/></svg>
      <svg class="gallery-arrow" style="left:508px" width="12" height="20" viewBox="0 0 12 20"><polyline points="2,2 10,10 2,18" fill="none" stroke="#bbb" stroke-width="2"/></svg>
    </div>

    <footer class="site-footer">
      <span class="footer-mark"></span>
      <span>© 2016 by Edith Harrow.</span>
    </footer>
  </div>
</body>
</html>
```